Astrologer needs a design for business card

I need a business card design for my job in astrology and flower therapy.
In front side need the information add file.

In back side need the informations above:
INTERPRETAÇÕES
TENDÊNCIAS
AUTOCONHECIMENTO
ANÁLISE VOCACIONAL
DIRECIONAMENTO DE CARREIRA
RELACIONAMENTOS
ASTROLOGIA EMPRESARIAL
TERAPIA FLORAL – Florias de Dorsk e Rui Tavenco

Business

OVRA

```html
<!DOCTYPE html>
<html lang="pt">
<head>
<meta charset="utf-8">
<title>Astrologia e Florais – Cartão de Visita</title>
<link rel="stylesheet" href="https://fonts.googleapis.com/css2?family=Arimo:wght@400;700&family=Cinzel:wght@400&family=Itim&display=swap">
<style>
  :root {
    --page-bg: #e9e6e1;
    --green: #1d8a3c;
    --green-dark: #15702f;
    --green-glow: #2fa04c;
    --blue: #3438b0;
    --blue-light: #5a63d4;
    --blue-dark: #2a2c95;
    --yellow: #f7f21c;
    --white: #ffffff;
    --line: rgba(255,255,255,0.85);
  }
  * { box-sizing: border-box; margin: 0; padding: 0; }
  html, body { width: 1200px; height: 1200px; overflow: hidden; }
  body {
    background: var(--page-bg);
    position: relative;
    font-family: "Arimo", Arial, sans-serif;
  }
  .card {
    position: absolute;
    left: 150px;
    width: 900px;
    height: 500px;
    overflow: hidden;
    box-shadow: 0 6px 18px rgba(0,0,0,0.18);
    color: var(--white);
  }
  /* Back side: services list */
  .card-back { top: 80px; background: var(--green); }
  .card-back .wheel-decoration {
    position: absolute;
    right: -170px; top: -60px;
    width: 620px; height: 620px;
    border-radius: 50%;
    background: radial-gradient(circle, var(--green) 28%, var(--green-glow) 45%, var(--green-dark) 60%, var(--green) 72%);
    opacity: 0.55;
  }
  .services-title {
    position: absolute;
    left: 70px; top: 62px;
    font-family: "Arimo", Arial, sans-serif;
    font-weight: 700;
    font-size: 22px;
    color: var(--yellow);
    letter-spacing: 0.3px;
    padding-bottom: 6px;
    border-bottom: 1.5px solid var(--line);
    padding-right: 14px;
  }
  .services-list {
    position: absolute;
    left: 70px; top: 112px;
    list-style: none;
  }
  .services-list li {
    display: flex;
    align-items: center;
    height: 40px;
    font-family: "Itim", cursive;
    font-size: 24px;
    letter-spacing: 1.5px;
  }
  .services-list .glyph {
    width: 46px;
    font-family: "DejaVu Sans", "Segoe UI Symbol", sans-serif;
    font-size: 22px;
  }
  .services-list .note { letter-spacing: 0.5px; }

  /* Front side: identity */
  .card-front {
    top: 620px;
    background: radial-gradient(ellipse at 60% 45%, var(--blue-light) 0%, var(--blue) 55%, var(--blue-dark) 100%);
  }
  .card-front .chart-illustration {
    position: absolute;
    left: -60px; top: 60px;
    width: 1020px; height: 1020px;
    border-radius: 50%;
    background: radial-gradient(circle, rgba(170,180,255,0.05) 30%, rgba(190,200,255,0.28) 48%, rgba(170,180,255,0.08) 56%, rgba(190,200,255,0.22) 62%, rgba(0,0,0,0) 70%);
  }
  .brand-heading {
    position: absolute;
    left: 0; right: 0; top: 48px;
    display: flex;
    align-items: center;
  }
  .brand-heading .rule { height: 1.5px; background: var(--line); }
  .brand-heading .rule-left { width: 42px; margin-right: 12px; }
  .brand-heading .rule-right { flex: 1; margin-left: 12px; margin-right: 40px; }
  .brand-heading h1 {
    font-family: "Cinzel", Georgia, serif;
    font-weight: 400;
    font-size: 44px;
    letter-spacing: 1px;
    white-space: nowrap;
  }
  .zodiac-row {
    position: absolute;
    left: 56px; top: 112px;
    font-family: "DejaVu Sans", "Segoe UI Symbol", sans-serif;
    font-size: 22px;
    letter-spacing: 16px;
  }
  .contact {
    position: absolute;
    left: 56px; top: 318px;
  }
  .contact .name {
    font-family: "Arimo", Arial, sans-serif;
    font-weight: 700;
    font-size: 40px;
    color: var(--yellow);
    padding-right: 60px;
    padding-bottom: 4px;
    border-bottom: 1.5px solid var(--line);
    display: inline-block;
  }
  .contact-line {
    display: flex;
    align-items: center;
    margin-top: 10px;
    font-size: 25px;
  }
  .contact-line svg { width: 34px; height: 26px; }
  .contact-line .divider {
    width: 1.5px; height: 26px;
    background: var(--line);
    margin: 0 12px 0 10px;
  }
</style>
</head>
<body>

<section class="card card-back">
  <div class="wheel-decoration" role="img" aria-label="Faint astrological wheel decoration"></div>
  <h2 class="services-title">MAPAS ASTROLÓGICOS E TERAPIA FLORAL</h2>
  <ul class="services-list">
    <li><span class="glyph">♂&#xFE0E;</span>INTERPRETAÇÕES</li>
    <li><span class="glyph">♃&#xFE0E;</span>TENDÊNCIAS</li>
    <li><span class="glyph">☿&#xFE0E;</span>AUTOCONHECIMENTO</li>
    <li><span class="glyph">♀&#xFE0E;</span>ANÁLISE VOCACIONAL</li>
    <li><span class="glyph">♄&#xFE0E;</span>DIRECIONAMENTO DE CARREIRA</li>
    <li><span class="glyph">♇&#xFE0E;</span>RELACIONAMENTOS</li>
    <li><span class="glyph">♆&#xFE0E;</span>ASTROLOGIA EMPRESARIAL</li>
    <li><span class="glyph">☉&#xFE0E;</span>TERAPIA FLORAL&nbsp;&nbsp;-&nbsp;<span class="note">Florias de Dorsk e Rui Tavenco</span></li>
  </ul>
</section>

<section class="card card-front">
  <div class="chart-illustration" role="img" aria-label="Soft blurred astrological birth chart wheel"></div>
  <div class="brand-heading">
    <span class="rule rule-left"></span>
    <h1>ASTROLOGIA E FLORAIS</h1>
    <span class="rule rule-right"></span>
  </div>
  <div class="zodiac-row">♈&#xFE0E;♉&#xFE0E;♊&#xFE0E;♋&#xFE0E;♌&#xFE0E;♍&#xFE0E;♎&#xFE0E;♏&#xFE0E;♐&#xFE0E;♑&#xFE0E;♒&#xFE0E;♓&#xFE0E;</div>
  <div class="contact">
    <div class="name">Marina Velloso</div>
    <div class="contact-line">
      <svg viewBox="0 0 34 26" aria-hidden="true">
        <path d="M3 9 Q17 1 31 9 L28 13 L23 11 L22 8 Q17 6 12 8 L11 11 L6 13 Z" fill="#fff"/>
        <rect x="8" y="14" width="18" height="10" rx="2" fill="#fff"/>
        <circle cx="17" cy="19" r="3" fill="#3438b0"/>
      </svg>
      <span class="divider"></span>
      <span>(51)9382-5517</span>
    </div>
    <div class="contact-line">
      <svg viewBox="0 0 34 26" aria-hidden="true">
        <rect x="3" y="4" width="28" height="18" fill="none" stroke="#fff" stroke-width="2"/>
        <path d="M3 4 L17 15 L31 4 M3 22 L13 12 M31 22 L21 12" fill="none" stroke="#fff" stroke-width="2"/>
      </svg>
      <span class="divider"></span>
      <span>marinavelloso@mailbox.com</span>
    </div>
  </div>
</section>

</body>
</html>
```